Business Cards for wirefen.com.au
Logo already designed by Quillnoxa
Professional
Liam Forbury
Technical Engineer
Mobile: 0437 125 806
liam@wirefen.com.au
www.wirefen.com.au
Should have the text: "Cloud Application Development"

```html
<!DOCTYPE html>
<html lang="en">
<head>
<meta charset="utf-8">
<title>wirefen.com.au — Business Card</title>
<link rel="stylesheet" href="https://fonts.googleapis.com/css2?family=Arimo:wght@400;700&display=swap">
<style>
  :root {
    --page-bg: #dcdde0;
    --card-bg: #ffffff;
    --blue-light: #3fb0ea;
    --blue-mid: #1f7fcf;
    --blue-deep: #143f8f;
    --ink: #3a3d42;
    --ink-soft: #5a5e66;
    --tagline: #4d6f9a;
    --swoosh: #c9ccd2;
    --watermark: #eef2f7;
  }
  html, body {
    margin: 0;
    width: 1200px;
    height: 1050px;
    overflow: hidden;
    background: var(--page-bg);
    font-family: "Arimo", Arial, sans-serif;
  }
  .card {
    position: absolute;
    left: 100px;
    top: 225px;
    width: 1000px;
    height: 600px;
    background: var(--card-bg);
    border-radius: 28px;
    overflow: hidden;
    box-shadow: 0 6px 18px rgba(0,0,0,0.18);
  }
  .card-art {
    position: absolute;
    inset: 0;
    width: 1000px;
    height: 600px;
  }
  .holder {
    position: absolute;
    right: 70px;
    top: 70px;
    text-align: right;
    color: #ffffff;
  }
  .holder-name {
    font-weight: 700;
    font-size: 38px;
    letter-spacing: 0.5px;
    margin: 0;
  }
  .holder-role {
    font-size: 19px;
    margin: 6px 0 0;
  }
  .brand {
    position: absolute;
    left: 54px;
    top: 218px;
  }
  .brand-name {
    display: flex;
    align-items: center;
    gap: 12px;
    margin: 0;
    font-weight: 700;
    font-size: 62px;
    color: var(--ink);
    letter-spacing: -0.5px;
    line-height: 1;
  }
  .brand-dot {
    width: 20px;
    height: 20px;
    border-radius: 50%;
    background: var(--blue-mid);
  }
  .brand-tagline {
    margin: 10px 0 0;
    font-size: 34px;
    color: var(--tagline);
    letter-spacing: 0.3px;
  }
  .contact {
    position: absolute;
    left: 54px;
    top: 468px;
    font-size: 21px;
    color: var(--ink-soft);
    border-collapse: collapse;
  }
  .contact td {
    padding: 2px 0;
  }
  .contact .label {
    width: 78px;
  }
</style>
</head>
<body>
  <section class="card">
    <svg class="card-art" viewBox="0 0 1000 600" aria-hidden="true">
      <defs>
        <linearGradient id="bandGradient" x1="0" y1="0" x2="1" y2="0">
          <stop offset="0" stop-color="var(--blue-light)"/>
          <stop offset="0.55" stop-color="var(--blue-mid)"/>
          <stop offset="1" stop-color="var(--blue-deep)"/>
        </linearGradient>
      </defs>
      <circle class="watermark" cx="870" cy="520" r="190" fill="var(--watermark)"/>
      <path class="header-band" d="M0 0 H1000 V300 C760 175 420 108 0 96 Z" fill="url(#bandGradient)"/>
      <path class="swoosh-line" d="M0 118 C420 130 760 200 1000 322" fill="none" stroke="var(--swoosh)" stroke-width="5"/>
    </svg>

    <header class="holder">
      <p class="holder-name">Liam Forbury</p>
      <p class="holder-role">Technical Engineer</p>
    </header>

    <div class="brand">
      <p class="brand-name"><span>wirefen.com.au</span><span class="brand-dot"></span></p>
      <p class="brand-tagline">Cloud Application Development</p>
    </div>

    <table class="contact">
      <tr><td class="label">Mobile</td><td>: 0437 125 806</td></tr>
      <tr><td class="label">Email</td><td>: liam@wirefen.com.au</td></tr>
      <tr><td class="label">Web</td><td>: www.wirefen.com.au</td></tr>
    </table>
  </section>
</body>
</html>
```